EPIC, awesome, creative business card needed - get involved!

I'm launching a boutique, exclusive Property Management real estate agency in Sydney early next year.
The name of the agency will be called "Quartz Hill Lane" - it's a play on "chase the silver pebble trail" to wealth. The Quartz Hill Lane signifies wealth through property investment.
My business will offer management of investment properties (ie Property Management).
The difference with Quartz Hill Lane and other agencies is the business will be run by one of Australia's leading property investment experts, and also one of Australia's leading property managers.
It will be exclusively for high net worth properties and individuals, so the business card needs to be extremely sharp, slick and relatively simple.
The information I want on the card is as follows
Nolan Pryce - Director
M: 0412 967 154
P: 9735 6021
E: nolan@quartzhilllane.net.au
W: quartzhilllane.net.au
I'm happy with the red from the logo, black - no yellows or funky colors. I want this to be a super corporate and slick business card to match the high end nature of the business.
Good luck everyone, and please ask questions for clarification.

```html
<!DOCTYPE html>
<html lang="en">
<head>
<meta charset="utf-8">
<title>Quartz Hill Lane — Business Card</title>
<link href="https://fonts.googleapis.com/css2?family=Barlow+Condensed:wght@400;500;700&display=swap" rel="stylesheet">
<style>
  :root {
    --brand-red: #ac1618;
    --paper-white: #fbfbfa;
    --backdrop: #e6e6e6;
    --ink-white: #ffffff;
    --rule: rgba(255, 255, 255, 0.55);
  }
  * { box-sizing: border-box; margin: 0; padding: 0; }
  html, body {
    width: 1200px;
    height: 795px;
    overflow: hidden;
  }
  body {
    background: var(--backdrop);
    font-family: "Barlow Condensed", "Arial Narrow", sans-serif;
    display: flex;
    align-items: center;
    justify-content: center;
    gap: 64px;
  }
  .card {
    position: relative;
    width: 460px;
    height: 336px;
    box-shadow: 0 14px 30px rgba(0, 0, 0, 0.18);
  }

  /* Front: contact side */
  .card--contact {
    background: var(--brand-red);
    color: var(--ink-white);
  }
  .holder {
    position: absolute;
    left: 40px;
    top: 40px;
  }
  .holder__name {
    font-size: 26px;
    font-weight: 500;
    letter-spacing: 0.06em;
    text-transform: uppercase;
    line-height: 1;
  }
  .holder__role {
    margin-top: 6px;
    font-size: 14px;
    font-weight: 400;
    letter-spacing: 0.14em;
    text-transform: uppercase;
  }
  .contact-list {
    position: absolute;
    right: 40px;
    bottom: 38px;
    width: 250px;
    list-style: none;
    font-size: 19px;
    font-weight: 400;
  }
  .contact-list li {
    display: flex;
    gap: 14px;
    padding: 5px 0 4px;
    border-bottom: 1px solid var(--rule);
  }
  .contact-list li:first-child { border-top: 1px solid var(--rule); }
  .contact-list .label { width: 54px; }

  /* Back: brand side */
  .card--brand {
    background: var(--paper-white);
  }
  .brand-mark {
    position: absolute;
    left: 52px;
    top: 50px;
    display: flex;
    align-items: flex-start;
    gap: 12px;
  }
  .brand-mark__square {
    width: 18px;
    height: 18px;
    background: var(--brand-red);
    margin-top: 6px;
  }
  .brand-mark__name {
    color: var(--brand-red);
    font-size: 34px;
    font-weight: 700;
    line-height: 0.95;
    text-transform: uppercase;
    letter-spacing: 0.02em;
  }
  .web-address {
    position: absolute;
    right: 44px;
    bottom: 40px;
    color: var(--brand-red);
    font-size: 20px;
    font-weight: 500;
    letter-spacing: 0.12em;
  }
</style>
</head>
<body>
  <section class="card card--contact" aria-label="Business card front">
    <div class="holder">
      <p class="holder__name">Nolan Pryce</p>
      <p class="holder__role">Director</p>
    </div>
    <ul class="contact-list">
      <li><span class="label">Mobile:</span><span>0412 967 154</span></li>
      <li><span class="label">Phone:</span><span>9735 6021</span></li>
      <li><span class="label">Email:</span><span>nolan@quartzhilllane.net.au</span></li>
    </ul>
  </section>

  <section class="card card--brand" aria-label="Business card back">
    <div class="brand-mark">
      <span class="brand-mark__square" aria-hidden="true"></span>
      <p class="brand-mark__name">Quartz<br>Hill<br>Lane</p>
    </div>
    <p class="web-address">quartzhilllane.net.au</p>
  </section>
</body>
</html>
```